New Design required for Disposable Gloves Pack

We need a new design for our range of disposable Gloves.
The brand name is "Pardo" I will attach the existing logo.

The needs to be 3 variations of the design (maybe different colours) that we can use for the different kinds of gloves: Latex Gloves, Clear Vinyl Gloves & Blue Vinyl Gloves.
Pack size is: 220x65x120mm.

Attached is a template to use showing all sides of the pack as flat. It is preferable that you supply an image of the complete folded pack as well with your design. Also attached is a PDF of our old pack design. Please use all the text on this old design for the new one.

The packs need to be easily differentiated from each other.

Target Market(s)

New Zealand Businesses, food processors & manufacturers. Medical & health care professionals

Font styles to use
Sans Serif

Requirements
Must have
• 3 variations of the same pack design to differentiate between the 3 types of gloves we offer: Latex Gloves, Clear Vinyl & Blue Vinyl Gloves.

```html
<!DOCTYPE html>
<html lang="en">
<head>
<meta charset="utf-8">
<title>Pardo Blue Vinyl Gloves – Carton Dieline</title>
<link rel="stylesheet" href="https://fonts.googleapis.com/css2?family=Archivo:ital,wght@1,900&family=Arimo:ital,wght@0,400;0,700;1,700&display=swap">
<style>
  :root {
    --carton-blue: #0763b3;
    --brand-green: #72a03f;
    --size-yellow: #fff200;
    --glow-white: #ffffff;
    --panel-text: #ffffff;
    --lizard-teal: #3f8a8c;
  }
  html, body {
    margin: 0;
    width: 1200px;
    height: 1200px;
    overflow: hidden;
    background: #ffffff;
  }
  .dieline { display: block; width: 1200px; height: 1200px; }
  .carton-fill { fill: var(--carton-blue); }
  .swoosh { fill: var(--brand-green); }
  .size-band { fill: var(--size-yellow); }
  .lizard-mark { fill: var(--lizard-teal); opacity: 0.8; }
  .brand-name { font-family: "Arimo", sans-serif; font-weight: 400; fill: var(--panel-text); letter-spacing: 1px; }
  .title-box { fill: var(--carton-blue); stroke: var(--glow-white); stroke-width: 1.5; }
  .title-top { font-family: "Archivo", sans-serif; font-style: italic; font-weight: 900; fill: var(--panel-text); }
  .title-main { font-family: "Archivo", sans-serif; font-style: italic; font-weight: 900; fill: var(--brand-green); stroke: var(--glow-white); stroke-width: 0.8; }
  .size-label { font-family: "Arimo", sans-serif; font-style: italic; font-weight: 700; fill: var(--carton-blue); }
  .feature-list { font-family: "Arimo", sans-serif; fill: var(--panel-text); }
  .dispense-window { fill: none; stroke: #6fa6da; stroke-width: 1; }
  .reorder-box { fill: #5a8fcb; }
  .reorder-text { font-family: "Arimo", sans-serif; fill: var(--panel-text); }
  .contact-text { font-family: "Arimo", sans-serif; font-weight: 700; fill: var(--panel-text); }
</style>
</head>
<body>
<svg class="dieline" viewBox="10 430 1480 1480" xmlns="http://www.w3.org/2000/svg">
  <defs>
    <radialGradient id="panel-glow" cx="0.5" cy="0.5" r="0.5">
      <stop offset="0" stop-color="#ffffff" stop-opacity="0.95"/>
      <stop offset="0.55" stop-color="#ffffff" stop-opacity="0.45"/>
      <stop offset="1" stop-color="#ffffff" stop-opacity="0"/>
    </radialGradient>
    <linearGradient id="hand-tone" x1="0" y1="0" x2="0" y2="1">
      <stop offset="0" stop-color="#ffffff"/>
      <stop offset="1" stop-color="#e6eef7"/>
    </linearGradient>
    <clipPath id="face-clip"><rect width="457" height="140"/></clipPath>
    <clipPath id="end-clip"><rect width="240" height="145"/></clipPath>

    <!-- Face branding: background, glow, swoosh, name, title, size (457 x 140) -->
    <g id="face-core" clip-path="url(#face-clip)">
      <rect class="carton-fill" width="457" height="140"/>
      <ellipse cx="170" cy="62" rx="230" ry="48" fill="url(#panel-glow)"/>
      <path class="swoosh" d="M335,0 C330,38 372,36 402,46 C430,56 442,76 457,92 V0 Z"/>
      <text class="brand-name" x="372" y="40" font-size="19">Pardo</text>
      <rect class="title-box" x="64" y="17" width="164" height="25" transform="skewX(-10)"/>
      <text class="title-top" x="66" y="38" font-size="20">BLUE VINYL</text>
      <text class="title-main" x="60" y="78" font-size="35">GLOVES</text>
      <rect class="size-band" x="0" y="81" width="160" height="15"/>
      <text class="size-label" x="58" y="94" font-size="14">Large</text>
    </g>

    <!-- Full face with hand and features -->
    <g id="face-art">
      <use href="#face-core"/>
      <rect x="244" y="40" width="64" height="100" rx="14" fill="url(#hand-tone)" role="img" aria-label="White illustration of a gloved hand"/>
      <text class="feature-list" x="313" y="94" font-size="10">Ambidexterous</text>
      <text class="feature-list" x="313" y="107" font-size="10">Single use</text>
      <text class="feature-list" x="313" y="120" font-size="10">Lightly powered</text>
    </g>

    <!-- End panel artwork: 240 x 145 -->
    <g id="end-art" clip-path="url(#end-clip)">
      <rect class="carton-fill" width="240" height="145"/>
      <ellipse cx="90" cy="90" rx="140" ry="46" fill="url(#panel-glow)"/>
      <rect class="lizard-mark" x="150" y="12" width="70" height="50" rx="22" role="img" aria-label="Lizard silhouette decoration"/>
      <rect class="title-box" x="42" y="62" width="110" height="17" transform="skewX(-10)"/>
      <text class="title-top" x="30" y="76" font-size="14">BLUE VINYL</text>
      <text class="title-main" x="26" y="101" font-size="23">GLOVES</text>
      <rect class="size-band" x="0" y="104" width="80" height="11"/>
      <text class="size-label" x="26" y="114" font-size="10">Large</text>
      <rect class="reorder-box" x="178" y="78" width="52" height="18"/>
      <text class="reorder-text" x="182" y="87" font-size="6">Reorder Code</text>
      <text class="contact-text" x="234" y="118" font-size="6" text-anchor="end">0800 555 019</text>
      <text class="contact-text" x="234" y="127" font-size="6" text-anchor="end">www.harbourpack.co.nz</text>
    </g>
  </defs>

  <!-- Top panel (lid), branding printed upside down -->
  <g class="panel-top">
    <rect class="carton-fill" x="58" y="880" width="457" height="285"/>
    <use href="#face-core" transform="translate(515 1165) rotate(180)"/>
    <rect x="192" y="920" width="64" height="110" rx="14" fill="url(#hand-tone)" role="img" aria-label="White illustration of a gloved hand, upside down"/>
    <g transform="rotate(180 143 967)">
      <text class="feature-list" x="101" y="952" font-size="11">Ambidexterous</text>
      <text class="feature-list" x="101" y="969" font-size="11">Single use</text>
      <text class="feature-list" x="101" y="986" font-size="11">Lightly powered</text>
    </g>
    <rect class="lizard-mark" x="365" y="925" width="125" height="75" rx="30" role="img" aria-label="Lizard silhouette decoration"/>
    <rect class="dispense-window" x="170" y="1004" width="238" height="56" rx="14"/>
  </g>

  <!-- Front panel + bottom flap -->
  <g class="panel-front">
    <use href="#face-art" x="58" y="1165"/>
    <path class="carton-fill" d="M58,1305 H515 V1460 H402 V1415 H175 V1460 H58 Z"/>
  </g>

  <!-- End panel one -->
  <g class="panel-end">
    <path class="carton-fill" d="M522,1035 H745 L757,1162 H518 Z"/>
    <use href="#end-art" x="515" y="1160"/>
    <path class="carton-fill" d="M518,1305 H757 V1460 H650 V1388 Z"/>
  </g>

  <!-- Back panel -->
  <g class="panel-back">
    <use href="#face-art" x="752" y="1160"/>
    <path class="carton-fill" d="M757,1300 H1207 L1093,1415 V1460 H870 V1415 L757,1300 Z"/>
  </g>

  <!-- End panel two -->
  <g class="panel-end">
    <path class="carton-fill" d="M1212,1035 H1440 L1455,1162 H1207 Z"/>
    <use href="#end-art" x="1207" y="1158"/>
    <rect class="carton-fill" x="1447" y="1158" width="8" height="147"/>
    <path class="carton-fill" d="M1207,1303 H1455 V1388 L1320,1388 V1460 H1207 Z"/>
  </g>
</svg>
</body>
</html>
```